Weather of the Heart Is the Ledger A Novel by Carl Whitby and Martin Holloway

Weather of the Heart Is the Ledger is a business novel about leadership, follower-ship, resilience, and insight.
It follows a high-performing executive whose conventional management tools and techniques stop working during a professional crisis. His transformation does not come from new strategies or tactics, but from a fundamentally different understanding of how mindset shapes performance, decision-making, leadership and follower-ship. Through the course of the book, the executive, his team, and his customers realize that “State of Mind” (healthy psychological functioning) is the horsepower that drives business and life.
This is not a self-help book, textbook, or memoir. It is thoughtful business fiction with philosophical depth.

Introduction/Preface for the novel:
We wrote this book because something profound changed the way we live, work, and lead. Over the course of several decades - across boardrooms, high-stakes corporate challenges, private practice, and moments of quiet personal insight - we began to see a deeper truth about the human experience. It was a truth that, once seen, dramatically improved the quality of our lives, and the lives of the people with whom we worked.
That truth comes from understanding the Three Principles of Mind, Consciousness, and Thought, as discovered and first articulated by the philosopher and theosopher, Edwin Thorley. Though simple, these Principles point to something universally powerful—how all people experience life from the inside out. When understood, they reveal a level of clarity, resilience, and well-being that can transform not only individuals, but entire organizations.
At first, we tried to write a traditional business book—a primer designed to share how understanding the Principles can lead to more grounded, wise, and effective leadership—without the need for techniques or tools. But as we wrote, we found ourselves returning again and again to stories. Real stories. Composite stories. Fictional ones. We realized that the best way to share this understanding wasn’t through frameworks or prescriptive advice. It was through story.
So, we created one big story.
This novel is the result. Though fictional, it is inspired by real patterns, real shifts, and real struggles we’ve lived through and witnessed over decades of work, together and separately. The characters are inventions, but their experiences are familiar. We’ve watched people just like them transform—from confusion to clarity, from fear to resilience, from burnout to wisdom.
Our hope is that this book moves you—not just as a story, but as an experience. We believe that the ideas woven into Owen Castell’s journey can help anyone live with greater ease, purpose, and peace of mind. Whether you lead a Fortune 500 company or a family of five, what’s offered here is for you.
And if something in this story helps you see your own life with fresh eyes, then the book has done its job.
Welcome to the journey.
—Carl & Martin

Target Market(s)

• Senior leaders, executives, and high-potential managers • Business professionals experiencing pressure, burnout, or diminishing returns from traditional leadership approaches • Leadership coaches and organizational consultants • Readers of intelligent, reflective business fiction or non-business people who are interested in what makes people tick — and achieve their highest potential Tone should appeal to serious, experienced professionals, not beginners or hype-seekers.

Industry/Entity Type

• Business / Leadership / Psychology • Business Fiction • Leadership Novel

Font styles to use
Serif

Colors
0054AA
0677BA
7BADD7
CADEEF
E8F1F8

Requirements
Must have
• We are looking for metaphorical representations of: • A fork in the road • A deviation from the conventional path (that makes all the difference) • One element choosing a different direction—not running away, not rebelling, just seeing differently Think quiet insight, not drama. Must-Haves • Clear, legible title at thumbnail size • A visual metaphor for choice or alternate thinking • Professional, credible aesthetic • Obvious that this is fiction (a novel), not a textbook • Clean typography (no clutter)
Nice to have
• • A sense of motion or transition • Minimalist or restrained color palette • One accent element that signifies insight or departure from convention • Timeless design (should still feel current in 5 or 10 years)
Should not have
• • Literal business clichés (gears, ladders, chess pieces, lightbulbs, compasses, eagles) • Stock-photo people in suits • “Hero CEO” imagery • Overly mystical or “woo-woo” visuals • Aggressive, macho, or hustle-culture tone • Anything cartoonish or silly

```html
<!DOCTYPE html>
<html lang="en">
<head>
<meta charset="utf-8">
<title>Weather of the Heart Is the Ledger — Cover Concept</title>
<link rel="stylesheet" href="https://fonts.googleapis.com/css2?family=Montserrat:wght@300;600;700&display=swap">
<style>
  :root {
    --paper: #ffffff;
    --cover-blue: #0054aa;
    --ink-light: #ffffff;
    --label-ink: #2b2b2b;
  }
  * { margin: 0; padding: 0; box-sizing: border-box; }
  html, body {
    width: 898px;
    height: 1200px;
    overflow: hidden;
    background: var(--paper);
  }
  .sheet {
    position: relative;
    width: 898px;
    height: 1200px;
    background: var(--paper);
    font-family: "Montserrat", Arial, sans-serif;
  }
  .cover {
    position: absolute;
    left: 180px;
    top: 153px;
    width: 539px;
    height: 865px;
    background: var(--cover-blue);
    overflow: hidden;
  }
  .cover-art {
    position: absolute;
    left: 0;
    top: 0;
    width: 539px;
    height: 865px;
  }
  .title-word { fill: var(--ink-light); font-family: "Montserrat", Arial, sans-serif; font-weight: 700; }
  .insight-dot { fill: var(--ink-light); }
  .byline {
    position: absolute;
    left: 51px;
    top: 769px;
    color: var(--ink-light);
    text-transform: uppercase;
    line-height: 1;
  }
  .byline-label {
    display: block;
    font-weight: 300;
    font-size: 16px;
    letter-spacing: 0.3px;
  }
  .byline-authors {
    display: block;
    margin-top: 6px;
    font-weight: 600;
    font-size: 19px;
    letter-spacing: 0.2px;
    white-space: nowrap;
  }
  .concept-label {
    position: absolute;
    left: 180px;
    top: 1041px;
    color: var(--label-ink);
    font-weight: 700;
    font-size: 23px;
    letter-spacing: 0.4px;
    line-height: 1;
  }
</style>
</head>
<body>
  <main class="sheet">
    <section class="cover" aria-label="Book cover: Weather of the Heart Is the Ledger, a novel by Carl Whitby and Martin Holloway">
      <svg class="cover-art" viewBox="0 0 539 865" xmlns="http://www.w3.org/2000/svg" aria-hidden="true">
        <circle class="insight-dot" cx="348" cy="230" r="25"/>
        <g transform="scale(-1,1)">
          <text class="title-word" x="-346" y="566" font-size="56" textLength="295" lengthAdjust="spacingAndGlyphs">WEATHER</text>
        </g>
        <text class="title-word" x="51" y="630" font-size="56" textLength="442" lengthAdjust="spacingAndGlyphs">OF THE HEART</text>
        <text class="title-word" x="51" y="655" font-size="21" textLength="438" lengthAdjust="spacing">IS THE LEDGER</text>
      </svg>
      <h1 style="position:absolute;width:1px;height:1px;overflow:hidden;clip:rect(0 0 0 0);">Weather of the Heart Is the Ledger</h1>
      <p class="byline">
        <span class="byline-label">A Novel by</span>
        <span class="byline-authors">Carl Whitby and Martin Holloway</span>
      </p>
    </section>
    <p class="concept-label">CONCEPT DESIGN</p>
  </main>
</body>
</html>
```